Marrowby Lane School bookmark

We need a vertical card (DL 99x210 mm) that will be put inside books at a primary school for children to make comments about the books. Text at the top:
Marrowby Lane School (and logo)
What did you think of this book?

Text at the bottom:
Pass it on!

Words in repeated pattern around the edge: funny sad exciting mysterious fantastic boring enthralling interesting

It should be in interesting bright colours with a white or pale background as children will write on the cards

The card should be double sided with the same design on each side

Industry/Entity Type

School

```html
<!DOCTYPE html>
<html lang="en">
<head>
<meta charset="utf-8">
<title>Marrowby Lane School bookmark</title>
<link rel="stylesheet" href="https://fonts.googleapis.com/css2?family=Short+Stack&family=Indie+Flower&display=swap">
<style>
  :root {
    --sky-top: #ffffff;
    --sky-mid: #e6f4fb;
    --sea: #c3e5f7;
    --paper: #ffffff;
    --bubble: #ffffff;
    --orange: #f7941d;
    --red: #e8262a;
    --badge-red: #d8262b;
    --ink: #111111;
    --rule: #8c8c8c;
    --fish: #fcc419;
    --w-blue: #2a7fd4;
    --w-sky: #2aa6df;
    --w-red: #e8443a;
    --w-pink: #e0457b;
    --w-purple: #7b3fa0;
    --w-green: #2e9e5b;
    --w-orange: #f08a24;
    --w-grey: #777777;
  }
  * { margin: 0; padding: 0; box-sizing: border-box; }
  html, body { width: 1200px; height: 2544px; overflow: hidden; }
  .bookmark {
    position: relative;
    width: 1200px;
    height: 2544px;
    overflow: hidden;
    background: linear-gradient(to bottom, var(--sky-top) 0%, var(--sky-top) 18%, var(--sky-mid) 40%, var(--sea) 75%, var(--sea) 100%);
    font-family: "Short Stack", "Comic Sans MS", cursive;
  }
  .writing-pool {
    position: absolute;
    left: -191px;
    top: 735px;
    width: 1582px;
    height: 1582px;
    border-radius: 50%;
    background: var(--paper);
  }
  .school-badge {
    position: absolute;
    left: 466px;
    top: -17px;
    width: 268px;
    height: 268px;
    border-radius: 50%;
    background: var(--badge-red);
  }
  .school-name {
    position: absolute;
    top: 370px;
    left: 0;
    width: 1200px;
    text-align: center;
    font-size: 44px;
    font-weight: 400;
    white-space: nowrap;
    color: var(--ink);
  }
  .prompt {
    position: absolute;
    top: 528px;
    left: 0;
    width: 1200px;
    text-align: center;
    font-size: 57px;
    font-weight: 400;
    white-space: nowrap;
    color: var(--orange);
  }
  .write-lines { position: absolute; left: 0; top: 0; }
  .write-lines line { stroke: var(--rule); stroke-width: 3; stroke-dasharray: 20 14; }
  .bubble { position: absolute; border-radius: 50%; background: var(--bubble); }
  .sign-off {
    position: absolute;
    left: 104px;
    top: 2318px;
    font-size: 104px;
    line-height: 1;
    white-space: nowrap;
    color: var(--red);
  }
  .fish {
    position: absolute;
    left: 842px;
    top: 2322px;
    width: 308px;
    height: 156px;
    border-radius: 50% 30% 30% 50%;
    background: var(--fish);
  }
  .mood {
    position: absolute;
    font-family: "Indie Flower", "Comic Sans MS", cursive;
    line-height: 1;
    white-space: nowrap;
    transform-origin: left center;
  }
</style>
</head>
<body>
<div class="bookmark">
  <div class="writing-pool"></div>

  <div class="school-badge" aria-hidden="true"></div>
  <h1 class="school-name">Marrowby Lane School</h1>
  <h2 class="prompt">What did you think of this book?</h2>

  <svg class="write-lines" width="1200" height="2544" aria-hidden="true">
    <line x1="131" y1="943" x2="1064" y2="943"/>
    <line x1="131" y1="1064" x2="1064" y2="1064"/>
    <line x1="131" y1="1187" x2="1064" y2="1187"/>
    <line x1="131" y1="1310" x2="1064" y2="1310"/>
    <line x1="131" y1="1435" x2="1064" y2="1435"/>
    <line x1="131" y1="1558" x2="1064" y2="1558"/>
    <line x1="131" y1="1685" x2="1064" y2="1685"/>
    <line x1="131" y1="1806" x2="1064" y2="1806"/>
    <line x1="131" y1="1936" x2="1064" y2="1936"/>
    <line x1="212" y1="2056" x2="965" y2="2056"/>
  </svg>

  <div class="bubble" style="left:172px;top:704px;width:68px;height:68px"></div>
  <div class="bubble" style="left:248px;top:2207px;width:68px;height:68px"></div>
  <div class="bubble" style="left:774px;top:2211px;width:38px;height:38px"></div>
  <div class="bubble" style="left:844px;top:2205px;width:64px;height:64px"></div>
  <div class="bubble" style="left:796px;top:2296px;width:46px;height:46px"></div>

  <p class="sign-off">Pass it on!</p>
  <div class="fish" role="img" aria-label="Smiling yellow fish with orange and red stripes"></div>

  <span class="mood" style="left:21px;top:30px;font-size:22px;color:var(--w-blue);transform:rotate(-3deg)">mysterious</span>
  <span class="mood" style="left:17px;top:125px;font-size:36px;color:var(--w-red);transform:rotate(-8deg)">boring</span>
  <span class="mood" style="left:24px;top:200px;font-size:48px;color:var(--w-red);transform:rotate(32deg)">exciting</span>
  <span class="mood" style="left:25px;top:365px;font-size:20px;color:var(--w-purple);transform:rotate(10deg)">fantastic</span>
  <span class="mood" style="left:25px;top:475px;font-size:20px;color:var(--w-green);transform:rotate(-5deg)">enthralling</span>
  <span class="mood" style="left:1035px;top:14px;font-size:34px;color:var(--w-orange);transform:rotate(20deg)">enthralling</span>
  <span class="mood" style="left:1117px;top:155px;font-size:40px;color:var(--w-blue);transform:rotate(-8deg)">sad</span>
  <span class="mood" style="left:1094px;top:244px;font-size:20px;color:var(--w-green);transform:rotate(30deg)">mysterious</span>
  <span class="mood" style="left:1071px;top:398px;font-size:34px;color:var(--w-red);transform:rotate(-15deg)">funny</span>
  <span class="mood" style="left:1077px;top:658px;font-size:30px;color:var(--w-blue);transform:rotate(-15deg)">fantastic</span>
  <span class="mood" style="left:1009px;top:740px;font-size:28px;color:var(--w-grey)">interesting</span>
  <span class="mood" style="left:1039px;top:812px;font-size:34px;color:var(--w-orange);transform:rotate(-10deg)">exciting</span>
  <span class="mood" style="left:42px;top:792px;font-size:32px;color:var(--w-sky);transform:rotate(-15deg)">funny</span>
  <span class="mood" style="left:32px;top:875px;font-size:30px;color:var(--w-pink)">sad</span>
  <span class="mood" style="left:38px;top:2084px;font-size:32px;color:var(--w-green);transform:rotate(5deg)">mysterious</span>
  <span class="mood" style="left:32px;top:2191px;font-size:28px;color:var(--w-orange);transform:rotate(-5deg)">enthralling</span>
  <span class="mood" style="left:1035px;top:2040px;font-size:32px;color:var(--w-purple);transform:rotate(-10deg)">fantastic</span>
  <span class="mood" style="left:1085px;top:2118px;font-size:26px;color:var(--w-orange)">boring</span>
  <span class="mood" style="left:1073px;top:2188px;font-size:36px;color:var(--w-red);transform:rotate(20deg)">funny</span>
  <span class="mood" style="left:32px;top:2464px;font-size:26px;color:var(--w-blue);transform:rotate(-10deg)">interesting</span>
</div>
</body>
</html>
```